Stainless Steel Water Bottle Packaging

We need a design for our cylindrical water bottle packaging.

Please see attached template (500ml cola bottle template .ai file) for exact dimensions.

VORO is defined as the elemental forces of nature embodied in an object or person. The design should be eye catching and draw potential clients in. Although its a cylindrical bottle/box, the front which would face the customer when sitting on a shelf should clearly display our logo.

Industry/Entity Type

Steel

Requirements
Must have
• Designed to the specifications of the attached template (see attached)
• Our VORO Logo (see attached) and website www.vorobottle.example(in smaller font) must appear.
• Size of bottle must appear - '17 oz/500 ml'
• These should appear somewhere:
• 'INULATED DOUBLE-WALL STAINLESS STEEL WATER BOTTLE'
• 'VORO Bottles magically keeps drinks cold for up to 24hrs, hot for 12',
• 'BPA Free'
• 'For every VORO bottle purchased, a portion of proceeds will go towards charity. Each of our colour's have been assigned a specific charity. Please visit www.vorobottle.example to find out which charity you helped support!'
• The Top circle - just our Symbol (flame/drop)
• The bottom circle - 'Inc. Designed in Canada made in China' on the outer edge leaving the middle empty for the UPC code.
• Reference website for the bottle case I'm looking for:
• http://shopkorinday.example/t-flow-lagoon-pink-insulated-water-bottle
Nice to have
• illustration of our water bottle shape (see attached) appearing somewhere on the box is something i had in mind but definitely not necessary.

```html
<!DOCTYPE html>
<html lang="en">
<head>
<meta charset="utf-8">
<title>VORO Bottle Packaging</title>
<link href="https://fonts.googleapis.com/css2?family=Questrial&family=Roboto+Condensed:wght@400&family=Arimo:wght@400;700&display=swap" rel="stylesheet">
<style>
  :root {
    --brand-blue: #39a8d8;
    --brand-blue-deep: #2a97c9;
    --band-blue: #3aa9d9;
    --paper: #ffffff;
    --paper-edge: #d7d9db;
    --canvas-bg: #ffffff;
    --bottle-tint: #eaf5fb;
  }
  html, body {
    margin: 0;
    padding: 0;
    width: 1200px;
    height: 1143px;
    overflow: hidden;
    background: var(--canvas-bg);
  }
  .canvas {
    position: relative;
    width: 1200px;
    height: 1143px;
  }
  .wrap-panel {
    position: absolute;
    top: 16px;
    width: 323px;
    height: 1108px;
    background: linear-gradient(90deg,
      var(--paper-edge) 0%, #f3f4f5 7%, var(--paper) 22%,
      var(--paper) 78%, #f3f4f5 93%, var(--paper-edge) 100%);
  }
  .wrap-panel--front { left: 282px; }
  .wrap-panel--back { left: 640px; }

  .brand-name {
    position: absolute;
    top: 112px;
    left: 0;
    width: 100%;
    text-align: center;
    font-family: "Questrial", sans-serif;
    font-size: 72px;
    letter-spacing: 4px;
    line-height: 1;
    color: var(--brand-blue);
  }
  .brand-dot {
    position: absolute;
    top: 60px;
    left: 150px;
    width: 22px;
    height: 22px;
    border-radius: 50%;
    background: var(--brand-blue);
  }

  .band {
    position: absolute;
    left: 0;
    width: 100%;
    background: var(--band-blue);
    color: #fff;
    text-align: center;
    font-family: "Arimo", sans-serif;
  }
  .band--top {
    top: 183px;
    height: 25px;
    line-height: 25px;
    font-size: 17px;
    font-weight: 700;
    letter-spacing: 2.4px;
  }
  .band--bottom {
    top: 1063px;
    height: 28px;
    line-height: 28px;
    font-size: 20px;
  }

  .bottle-art {
    position: absolute;
    top: 246px;
    left: 74px;
    width: 180px;
    height: 810px;
    border-radius: 40px 40px 60px 60px;
    background: linear-gradient(180deg, var(--bottle-tint), #f6fbfe);
  }
  .product-line {
    position: absolute;
    top: 378px;
    left: 150px;
    height: 670px;
    writing-mode: vertical-rl;
    transform: rotate(180deg);
    font-family: "Roboto Condensed", sans-serif;
    font-size: 20px;
    letter-spacing: 0.4px;
    color: var(--brand-blue-deep);
    white-space: nowrap;
    text-align: center;
  }

  .back-copy {
    position: absolute;
    left: 34px;
    width: 266px;
    font-family: "Questrial", sans-serif;
    font-size: 18px;
    line-height: 22px;
    color: var(--brand-blue);
    text-align: justify;
    text-align-last: center;
    margin: 0;
  }
  .back-copy--charity { top: 700px; }
  .back-copy--performance { top: 936px; }
</style>
</head>
<body>
<main class="canvas">
  <section class="wrap-panel wrap-panel--front">
    <span class="brand-dot" aria-hidden="true"></span>
    <div class="brand-name">VORO</div>
    <div class="band band--top">www.vorobottle.example</div>
    <div class="bottle-art" role="img" aria-label="Line illustration of the bottle shape"></div>
    <div class="product-line">INS ULATED DOUBLE-WALL STAINLESS STEEL WATER BOTTLE</div>
    <div class="band band--bottom">17 oz/500 ml</div>
  </section>

  <section class="wrap-panel wrap-panel--back">
    <div class="band band--top"></div>
    <p class="back-copy back-copy--charity">For every VORO bottle purchased, a portion of proceeds will go towards charity. Each of our colour's have been assigned a specific charity. Please visit www.vorobottle.example to find out which charity you helped support!</p>
    <p class="back-copy back-copy--performance">VORO Bottles magically keeps drinks cold for up to 24hrs, hot for 12'</p>
    <div class="band band--bottom">BPA Free</div>
  </section>
</main>
</body>
</html>
```